ROVA Pty Ltd Business Card

Looking for a simple yet eye-catching double-sided business card design using my company logo on one side and contact details on the other.

Target Market(s)

Government

Industry/Entity Type

Communication Systems Engineering

Contact Information for Business Card

ROVA Pty Ltd

Requirements
Nice to have
• Would be great to have a QR code so details can be scanned into contacts

```html
<!DOCTYPE html>
<html lang="en">
<head>
<meta charset="utf-8">
<title>ROVA Pty Ltd Business Card</title>
<link href="https://fonts.googleapis.com/css2?family=Poppins:wght@300;400;600;700&display=swap" rel="stylesheet">
<style>
  :root {
    --backdrop: #2b2f36;
    --card-light: #ffffff;
    --card-dark: #111111;
    --ink: #1b1b1b;
    --brand-slate: #3c4750;
    --rule: #8a8a8a;
    --silver: #e6e6e6;
    --silver-dim: #6a6a6a;
  }
  * { box-sizing: border-box; margin: 0; padding: 0; }
  html, body {
    width: 1200px; height: 900px; overflow: hidden;
    background: var(--backdrop);
    font-family: "Poppins", sans-serif;
  }
  .canvas { position: relative; width: 1200px; height: 900px; }
  .card {
    position: absolute; left: 260px; width: 680px; height: 390px;
    border-radius: 4px; overflow: hidden;
    box-shadow: 0 14px 30px rgba(0,0,0,.45);
  }
  .card--front { top: 40px; background: var(--card-light); }
  .card--back  { top: 470px; background: var(--card-dark); }

  /* front */
  .brand {
    position: absolute; left: 44px; top: 40px;
    display: flex; align-items: center; gap: 14px;
  }
  .brand__dot {
    width: 34px; height: 34px; border-radius: 50%;
    border: 2px solid var(--brand-slate);
  }
  .brand__name {
    font-weight: 700; font-size: 46px; letter-spacing: 4px;
    color: var(--brand-slate); line-height: 1;
  }
  .contact-list {
    position: absolute; left: 44px; top: 130px; list-style: none;
  }
  .contact-item {
    display: flex; align-items: center; gap: 12px;
    height: 40px; position: relative;
    font-size: 15px; font-weight: 400; color: var(--ink);
    white-space: nowrap;
  }
  .contact-item__icon {
    width: 24px; height: 24px; border-radius: 50%;
    border: 1.5px solid var(--ink);
    display: flex; align-items: center; justify-content: center;
    flex: none;
  }
  .contact-item__rule {
    position: absolute; left: 36px; bottom: 4px; height: 1px;
    background: var(--rule);
  }
  .circuit-art {
    position: absolute; right: 0; bottom: 0; width: 300px; height: 260px;
    background: linear-gradient(135deg, rgba(255,255,255,0) 0%, #d8d8d8 45%, #9a9a9a 100%);
    clip-path: polygon(100% 0, 100% 100%, 0 100%, 40% 45%);
  }

  /* back */
  .back-brand {
    position: absolute; left: 0; right: 0; top: 140px;
    display: flex; align-items: center; justify-content: center; gap: 18px;
  }
  .back-brand__dot {
    width: 40px; height: 40px; border-radius: 50%;
    border: 2px solid var(--silver-dim);
  }
  .back-brand__name {
    font-weight: 700; font-size: 72px; letter-spacing: 6px;
    color: var(--silver); line-height: 1;
  }
  .back-url {
    position: absolute; left: 0; right: 0; top: 260px; text-align: center;
    font-size: 13px; letter-spacing: 2px; color: var(--silver-dim);
  }
</style>
</head>
<body>
<main class="canvas">
  <section class="card card--front" aria-label="Card front with contact details">
    <div class="brand">
      <span class="brand__dot"></span>
      <span class="brand__name">ROVA</span>
    </div>
    <ul class="contact-list">
      <li class="contact-item">
        <span class="contact-item__icon">
          <svg width="12" height="12" viewBox="0 0 24 24"><path d="M6 2l4 4-2 3c1.5 3 4 5.5 7 7l3-2 4 4-3 4C10 21 3 14 2 5z" fill="#1b1b1b"/></svg>
        </span>
        5550-4821-907
        <span class="contact-item__rule" style="width:340px"></span>
      </li>
      <li class="contact-item">
        <span class="contact-item__icon">
          <svg width="12" height="12" viewBox="0 0 24 24"><rect x="2" y="5" width="20" height="14" fill="#1b1b1b"/><path d="M2 5l10 8 10-8" stroke="#fff" stroke-width="2" fill="none"/></svg>
        </span>
        admin@rova.com.au
        <span class="contact-item__rule" style="width:330px"></span>
      </li>
      <li class="contact-item">
        <span class="contact-item__icon">
          <svg width="12" height="12" viewBox="0 0 24 24"><circle cx="12" cy="12" r="10" fill="none" stroke="#1b1b1b" stroke-width="2"/><path d="M2 12h20M12 2c4 4 4 16 0 20M12 2c-4 4-4 16 0 20" stroke="#1b1b1b" stroke-width="2" fill="none"/></svg>
        </span>
        rova.com.au
        <span class="contact-item__rule" style="width:320px"></span>
      </li>
      <li class="contact-item">
        <span class="contact-item__icon">
          <svg width="12" height="12" viewBox="0 0 24 24"><path d="M12 2a7 7 0 017 7c0 5-7 13-7 13S5 14 5 9a7 7 0 017-7z" fill="#1b1b1b"/><circle cx="12" cy="9" r="2.5" fill="#fff"/></svg>
        </span>
        14-16 Harlow Street Elmvale WA, 6999 Australia
        <span class="contact-item__rule" style="width:400px"></span>
      </li>
    </ul>
    <div class="circuit-art" role="img" aria-label="Circuit board trace pattern rising from the lower right corner"></div>
  </section>

  <section class="card card--back" aria-label="Card back with company name">
    <div class="back-brand">
      <span class="back-brand__dot"></span>
      <span class="back-brand__name">ROVA</span>
    </div>
    <p class="back-url">ROVA.COM.AU</p>
  </section>
</main>
</body>
</html>
```